Financial PR company Homepage and Inner Page design

Please design a web homepage and innerpage for OVIN Public Relations.
OVIN Public Relations is a Financial PR company targeting Shenzhen Qian Special Economical Zone.
Note:
1. Menu includes ( Please specialize in Chinese and we want to see the Chinese fonts)
关于我们/服务板块/专业优势/合作伙伴/前海商圈/公司新闻/加盟我们/联系我们

2. Please refer to world class PR Business company and contribute your idea on website design and color themes.

3. We have attached the Logo for reference.

4. Anytime use picture for reference, please select asian business people pictures.

Cheers,

HI Designers, Thanks for the design submission. Here is our client feedback: 1. Adopt one screen design. 2. Use amiable Asia Business woman pictures. 3. Use contrastive color theme for the design. Cheers, Kip From TW

```html
<!DOCTYPE html>
<html lang="en">
<head>
<meta charset="utf-8">
<title>OVIN Public Relations</title>
<link href="https://fonts.googleapis.com/css2?family=Didact+Gothic&family=Open+Sans:wght@400;600;700&family=Arimo:wght@400;700&family=Noto+Sans+SC:wght@700&display=swap" rel="stylesheet">
<style>
  :root{
    --navy:#0f1d2e;
    --navy-logo:#13253a;
    --blue:#0aa0e6;
    --strip-dark:#121820;
    --white:#ffffff;
    --body-bg:#e1e1e1;
    --panel:#efefef;
    --text:#222222;
    --heading:#333333;
    --footer-top:#8c8c8c;
    --footer-bottom:#707070;
    --footer-soft:#e6e6e6;
  }
  *{margin:0;padding:0;box-sizing:border-box}
  html,body{width:1200px;height:1003px;overflow:hidden}
  body{position:relative;background:var(--body-bg);font-family:"Arimo",Arial,sans-serif}

  .site-header{position:absolute;left:0;top:0;width:1200px;height:91px;background:var(--navy)}
  .brand{position:absolute;left:132px;top:0;width:265px;height:91px;background:var(--navy-logo);display:flex;align-items:center;gap:14px;padding-left:14px}
  .brand-dot{width:38px;height:38px;border-radius:50%;background:var(--blue)}
  .brand-name{font-family:"Didact Gothic",sans-serif;color:var(--white);font-size:38px;letter-spacing:1px}
  .main-nav{position:absolute;left:397px;top:0;height:91px;display:flex;align-items:center;font-family:"Didact Gothic",sans-serif;font-size:12.5px;color:var(--white);text-transform:uppercase}
  .main-nav .current{background:var(--blue);height:91px;width:52px;display:flex;align-items:center;justify-content:center;margin-right:8px}
  .main-nav .sep{margin:0 6px}
  .client-area{position:absolute;left:970px;top:0;width:111px;height:22px;background:#f4f4f4;border-radius:0 0 4px 4px;color:#111;font-family:"Open Sans",sans-serif;font-size:13px;text-align:center;line-height:20px}

  .hero{position:absolute;left:0;top:91px;width:1200px;height:398px;background:linear-gradient(100deg,#4a86c4 0%,#8fb3d6 30%,#9aa6b3 50%,#3f4c66 70%,#9aa0a8 100%)}
  .hero-arrow{position:absolute;top:170px}

  .features{position:absolute;left:0;top:489px;width:1200px;height:108px;display:flex}
  .feature{position:relative;height:108px;background:var(--strip-dark);color:var(--white)}
  .feature.about{width:452px;background:linear-gradient(90deg,#0d1824,#1b2530)}
  .feature.strategy{width:304px;background:var(--blue)}
  .feature.team{width:444px;background:linear-gradient(90deg,#1a1f25,#111418)}
  .feature svg{position:absolute;top:36px}
  .feature h2{position:absolute;top:17px;font-family:"Open Sans",sans-serif;font-weight:700;font-size:16px;text-transform:uppercase}
  .feature p{position:absolute;top:42px;width:200px;font-family:"Open Sans",sans-serif;font-size:11.5px;line-height:15.5px}

  .welcome-card{position:absolute;left:131px;top:636px;width:937px;height:252px;background:var(--white);border-radius:8px;box-shadow:0 14px 14px -8px rgba(0,0,0,.35)}
  .welcome-panel{position:absolute;left:9px;top:10px;width:918px;height:232px;background:var(--panel);border-radius:4px}
  .welcome-panel h1{position:absolute;left:10px;top:18px;font-weight:400;font-size:20px;color:var(--heading)}
  .welcome-copy{position:absolute;left:10px;top:52px;width:608px;font-size:12.3px;line-height:20.4px;letter-spacing:.45px;color:var(--text)}
  .welcome-copy p+p{margin-top:20.4px}
  .welcome-photo{position:absolute;left:632px;top:61px;width:278px;height:131px;background:linear-gradient(180deg,#3a2a48 0%,#7a3a52 40%,#5c6a52 75%,#2a2c30 100%)}

  .site-footer{position:absolute;left:0;top:931px;width:1200px;height:72px;background:linear-gradient(180deg,var(--footer-top),var(--footer-bottom))}
  .footer-nav{position:absolute;left:145px;top:15px;font-family:"Noto Sans SC",sans-serif;font-weight:700;font-size:11px;color:var(--white);word-spacing:2px}
  .footer-nav .sep{margin:0 6px}
  .copyright{position:absolute;left:145px;top:42px;font-size:11.5px;color:var(--footer-soft)}
</style>
</head>
<body>
  <header class="site-header">
    <div class="brand"><span class="brand-dot"></span><span class="brand-name">OVIN PR</span></div>
    <nav class="main-nav">
      <span class="current">Home</span>About us<span class="sep">/</span>Service<span class="sep">/</span>Our advantage<span class="sep">/</span>Parters<span class="sep">/</span>Qianhai<span class="sep">/</span>Company news<span class="sep">/</span>Join us<span class="sep">/</span>Contact us
    </nav>
    <div class="client-area">Client Area</div>
  </header>

  <section class="hero" role="img" aria-label="Smiling Asian business team with a tablet beside celebrating colleagues in front of solar panels">
    <svg class="hero-arrow" style="left:160px" width="18" height="30" viewBox="0 0 18 30"><path d="M15 2 3 15l12 13" fill="none" stroke="#fff" stroke-width="4"/></svg>
    <svg class="hero-arrow" style="left:1024px" width="18" height="30" viewBox="0 0 18 30"><path d="M3 2l12 13L3 28" fill="none" stroke="#fff" stroke-width="4"/></svg>
  </section>

  <section class="features">
    <div class="feature about">
      <svg style="left:152px" width="50" height="46" viewBox="0 0 50 46" fill="none" stroke="#fff" stroke-width="3"><path d="M2 44V22h10V44M12 44V6h18v38M30 44V16h12v28M2 44h46"/><path d="M18 14h6M18 22h6M18 30h6" stroke-width="2"/></svg>
      <h2 style="left:232px">About us</h2>
      <p style="left:232px">Lorem Ipsum is simply dummy text of printing and typesetting indus Lorem Ipsum has been the standa</p>
    </div>
    <div class="feature strategy">
      <svg style="left:30px" width="40" height="50" viewBox="0 0 40 50" fill="#fff"><path d="M6 2h6v5h5V2h6v5h5V2h6v11l-5 4v20l5 5v6H4v-6l5-5V17l-5-4z"/><rect x="16" y="20" width="5" height="14" fill="#0aa0e6"/></svg>
      <h2 style="left:93px">Our strategy</h2>
      <p style="left:93px">Lorem Ipsum is simply dummy text of printing and typesetting indus Lorem Ipsum has been the standa</p>
    </div>
    <div class="feature team">
      <svg style="left:21px" width="62" height="44" viewBox="0 0 62 44" fill="#fff"><circle cx="14" cy="14" r="7"/><circle cx="48" cy="14" r="7"/><path d="M2 42c0-12 5-18 12-18s12 6 12 18zM36 42c0-12 5-18 12-18s12 6 12 18z"/><circle cx="31" cy="10" r="9" stroke="#15191e" stroke-width="2"/><path d="M16 44c0-15 7-23 15-23s15 8 15 23z" stroke="#15191e" stroke-width="2"/></svg>
      <h2 style="left:96px">Meet the team</h2>
      <p style="left:96px">Lorem Ipsum is simply dummy text of printing and typesetting indus Lorem Ipsum has been the standa</p>
    </div>
  </section>

  <main class="welcome-card">
    <div class="welcome-panel">
      <h1>Welcome to OVIN Public Relations</h1>
      <div class="welcome-copy">
        <p>Lorem ipsum dolor sit amet, consectetur adipiscing elit. Proin pulvinar eros in imperdiet porttitor. Praesent velit justo, placerat ut ornare aliquet, venenatis vel justo. Nulla porttitor enim vitae nibh scelerisque, nec laoreet libero posuere. Integer ut neque ut purus dictum auctor. Cras tincidunt odio a pharetra iaculis. Nam in arcu eu tortor consequat tempor. Vivamus eu convallis risus.</p>
        <p>Mauris pulvinar, eros ac elementum tempus, enim metus vehicula ante, ut scelerisque ipsum libero non sem. Integer a commodo augue. Ut accumsan efficitur mattis. Donec ut mollis nisl. Suspendisse tincidunt</p>
      </div>
      <div class="welcome-photo" role="img" aria-label="Classical stone columns of a financial building lit at dusk"></div>
    </div>
  </main>

  <footer class="site-footer">
    <nav class="footer-nav">关于我们<span class="sep"></span> 服务板块<span class="sep">/</span>专业优势<span class="sep">/</span>合作伙伴<span class="sep">/</span>前海商圈<span class="sep">/</span>公司新闻<span class="sep">/</span>加盟我们<span class="sep">/</span>联系我们</nav>
    <p class="copyright">Copyright © 2014 -&nbsp; OVIN Public Relations - All rights reserved.</p>
  </footer>
</body>
</html>
```